Veterinary Business cards

Redesign Business Card

Information needed on Card:
Hours: Mon-Fri: 4pm -10PM; Sat- Sun- 10 AM- 5PM
Help@bayfernvet.com
www.bayfernvet.com
555-718-2946
4173 SE 19th Ave. okc, ok 73958
*No appointment necessary*

Optional:
Our tag line is "We're here when you need us" - If it fits on the cards.

```html
<!DOCTYPE html>
<html lang="en">
<head>
<meta charset="utf-8">
<title>Bayfern Vet Urgent Care – Business Card</title>
<link href="https://fonts.googleapis.com/css2?family=Josefin+Sans:wght@300;400&family=Montserrat:wght@500;700&display=swap" rel="stylesheet">
<style>
  :root {
    --navy: #14365f;
    --orange: #e27c1c;
    --backdrop: #d9d9d9;
    --photo-light: #e6e6e6;
    --photo-mid: #9a9a9a;
    --photo-dark: #3a3a3a;
  }
  * { box-sizing: border-box; margin: 0; padding: 0; }
  html, body { width: 1200px; height: 846px; overflow: hidden; }
  body {
    background: var(--backdrop);
    font-family: "Josefin Sans", sans-serif;
    position: relative;
  }
  .card {
    position: absolute;
    top: 263px;
    width: 560px;
    height: 320px;
    background: var(--navy);
    overflow: hidden;
    box-shadow: 0 6px 18px rgba(0,0,0,0.18);
  }
  .card--front { left: 30px; }
  .card--back { left: 610px; }

  /* Front */
  .photo {
    position: absolute;
    top: 0;
    height: 100%;
  }
  .photo--cat {
    left: 0;
    width: 150px;
    background: linear-gradient(160deg, var(--photo-light) 0%, var(--photo-mid) 55%, var(--photo-dark) 100%);
  }
  .photo--owner-dog {
    right: 0;
    width: 165px;
    background: linear-gradient(200deg, var(--photo-light) 0%, var(--photo-mid) 45%, var(--photo-dark) 100%);
  }
  .divider {
    position: absolute;
    top: 0;
    width: 4px;
    height: 100%;
    background: var(--orange);
  }
  .divider--left { left: 150px; }
  .divider--right { right: 165px; }

  .info {
    position: absolute;
    left: 154px;
    right: 169px;
    top: 0;
    height: 100%;
    padding: 48px 20px 0 30px;
    color: var(--orange);
  }
  .brand-name {
    font-family: "Josefin Sans", sans-serif;
    font-weight: 400;
    color: var(--orange);
    line-height: 1.1;
  }
  .info .brand-name { font-size: 26px; }
  .contacts { list-style: none; margin-top: 28px; }
  .contacts li {
    display: flex;
    align-items: flex-start;
    gap: 10px;
    font-size: 17px;
    font-weight: 300;
    line-height: 1.15;
    margin-bottom: 7px;
  }
  .contacts svg { flex: 0 0 18px; width: 18px; height: 18px; margin-top: -1px; }

  /* Back */
  .brand-block {
    position: absolute;
    inset: 0;
    display: flex;
    flex-direction: column;
    align-items: center;
    justify-content: center;
    color: var(--orange);
    text-align: center;
  }
  .brand-block .brand-name { font-size: 38px; }
  .tagline {
    font-family: "Montserrat", sans-serif;
    font-weight: 700;
    font-size: 15px;
    letter-spacing: -0.3px;
    margin-top: 18px;
  }
  .hours {
    font-family: "Montserrat", sans-serif;
    font-weight: 500;
    font-size: 15px;
    margin-top: 22px;
  }
  .hours strong { font-weight: 700; }
  .no-appointment {
    font-family: "Montserrat", sans-serif;
    font-weight: 700;
    font-size: 15px;
    margin-top: 4px;
  }
</style>
</head>
<body>

<section class="card card--front">
  <div class="photo photo--cat" role="img" aria-label="Black and white close-up photo of a cat's eye and nose"></div>
  <div class="divider divider--left"></div>

  <div class="info">
    <p class="brand-name">Bayfern Vet<br>Urgent Care</p>

    <ul class="contacts">
      <li>
        <svg viewBox="0 0 24 24" fill="none" stroke="currentColor" stroke-width="2" stroke-linecap="round" stroke-linejoin="round"><path d="M5 3h4l2 5-2.5 1.5a11 11 0 0 0 6 6L16 13l5 2v4a2 2 0 0 1-2 2A16 16 0 0 1 3 5a2 2 0 0 1 2-2"/></svg>
        <span>555-718-2946</span>
      </li>
      <li>
        <svg viewBox="0 0 24 24" fill="none" stroke="currentColor" stroke-width="2" stroke-linejoin="round"><rect x="3" y="5" width="18" height="14"/><path d="M3 6l9 7 9-7"/></svg>
        <span>help@bayfernvet.com</span>
      </li>
      <li>
        <svg viewBox="0 0 24 24" fill="none" stroke="currentColor" stroke-width="2"><circle cx="12" cy="12" r="9"/><path d="M3 12h18M12 3c3 3 3 15 0 18M12 3c-3 3-3 15 0 18"/></svg>
        <span>www.bayfernvet.com</span>
      </li>
      <li>
        <svg viewBox="0 0 24 24" fill="none" stroke="currentColor" stroke-width="2" stroke-linejoin="round"><path d="M12 22s7-7 7-12a7 7 0 0 0-14 0c0 5 7 12 7 12z"/><circle cx="12" cy="10" r="2.5"/></svg>
        <span>4173 SE 19th Ave.<br>OKC, OK 73958</span>
      </li>
    </ul>
  </div>

  <div class="divider divider--right"></div>
  <div class="photo photo--owner-dog" role="img" aria-label="Black and white photo of a smiling woman hugging her dog"></div>
</section>

<section class="card card--back">
  <div class="brand-block">
    <p class="brand-name">Bayfern Vet Urgent Care</p>
    <p class="tagline">WE'RE HERE WHEN YOU NEED US</p>
    <p class="hours"><strong>Mon-Fri:</strong> 4pm-10pm <strong>Sat-Sun:</strong> 10am-5pm</p>
    <p class="no-appointment">NO APPOINTMENT NECESSARY</p>
  </div>
</section>

</body>
</html>
```